Web Design Project - (DESIGN AND FOLLOW UP CODING)

Web design for new management consultancy company

**About The Halvern Group

We work with organisations find and implement creative and sensible solutions...

We explore and inform…We have in-house research capability and enrich discussion through our own research, analysis and inputs. We interview staff and stakeholders, analyse data and literature and help you develop knowledge and solutions, and the plans to implement these.

We present new ideas…We develop proposals and reports that use internally and externally derived evidence to propose effective new solutions.

Specialties
Higher Education, TAFE, Local Government, Regional Development

Industry
Education Management
Updates

Target Market(s)

Business and government managers

Industry/Entity Type

Education

Requirements
Must have
• Sections:

**About
We work with organisations find and implement solutions to opportunities and challenges.
We explore and inform…
We present new ideas…

We develop proposals and reports that link internally and externally derived evidence to develop and implement new solutions.

Our three practice pillars are-
Ideas and partnerships:
Knowledgeable leaders:
Solutions:

** People
Martin Colbey (PHOTO) Bio

** Services
Acumen - Solutions - Partnerships -Implementation
- On time and within budget.
- Project leadership.
- Researched inputs and facilitated outcomes.
- Focus on implementation.
- Develop value-adding partnerships and get them funded
- Creative responses to funding opportunities
- Organisational reviews

Sectors
-Education
-State Government
- Local Government
- Utilities
- Financial services
- Health and ageing
- Human services
- Government
-Regional

** Careers

** Key Partners
With weblinks

** Contact

Links to Twitter LinkedIn Facebook
Nice to have
• Logo available from: quillmark@zevonet.com.au

```html
<!DOCTYPE html>
<html lang="en">
<head>
<meta charset="utf-8">
<title>The Halvern Group</title>
<link href="https://fonts.googleapis.com/css2?family=PT+Sans:wght@400;700&family=Roboto+Condensed:wght@400&display=swap" rel="stylesheet">
<style>
  :root{
    --orange:#f26532;
    --orange-dark:#e04e1c;
    --ink:#444;
    --text:#555;
    --muted:#6b6b6b;
    --line:#e6e6e6;
    --white:#fff;
  }
  *{box-sizing:border-box;margin:0;padding:0}
  html,body{width:1200px;height:1025px;overflow:hidden;background:var(--white);font-family:"PT Sans",sans-serif;color:var(--text)}
  .wrap{width:838px;margin:0 auto;position:relative}

  .site-header{height:81px}
  .site-header .wrap{height:81px;display:flex;align-items:center;justify-content:space-between}
  .brand{display:flex;align-items:center;gap:12px}
  .brand-mark{width:30px;height:30px;background:var(--orange)}
  .brand-name{font-weight:400;font-size:24px;color:var(--ink);line-height:1}
  .follow{display:flex;align-items:center;gap:4px;font-size:11px;color:var(--muted)}
  .follow span{margin-right:4px}
  .social{width:24px;height:24px;border-radius:50%}
  .s1{background:#2867b2}.s2{background:#3aa3df}.s3{background:#1c6f95}.s4{background:#f0a31c}

  .main-nav{background:var(--orange);height:43px}
  .main-nav ul{list-style:none;display:flex;height:43px;width:838px;margin:0 auto}
  .main-nav li{display:flex;align-items:center;justify-content:center;color:var(--white);font-size:11px;font-weight:700;text-transform:uppercase}
  .main-nav li.active{background:var(--orange-dark)}

  .hero{position:relative;height:426px;background:linear-gradient(100deg,#b9c4cc 0%,#d9dee0 35%,#c9d2d8 60%,#aebfd0 100%)}
  .hero-arrow{position:absolute;top:191px;width:48px;height:48px;border-radius:50%;border:2px solid rgba(120,90,70,.35)}
  .hero-arrow.prev{left:100px}.hero-arrow.next{left:1042px}
  .hero-arrow svg{width:100%;height:100%}
  .caption{position:absolute;left:181px;color:var(--white);font-family:"Roboto Condensed",sans-serif;font-size:24px;text-transform:uppercase;padding:0 16px;height:46px;display:flex;align-items:center}
  .caption.one{top:185px;background:rgba(226,96,56,.88)}
  .caption.two{top:244px;background:rgba(70,70,70,.78)}

  .welcome{text-align:center;padding-top:30px}
  .welcome h1{font-weight:400;font-size:16px;color:var(--orange);text-transform:uppercase}
  .welcome p{font-size:11px;line-height:19px;color:var(--muted);margin-top:12px}

  .pillars{display:flex;justify-content:space-between;margin-top:30px}
  .pillar{width:252px;text-align:center}
  .pillar svg{height:56px}
  .pillar h2{font-weight:400;font-size:16px;text-transform:uppercase;color:#555;margin-top:8px}
  .pillar p{font-size:9.4px;line-height:15.5px;color:var(--muted);margin-top:8px}
  .btn{display:inline-block;margin-top:14px;background:var(--orange);color:var(--white);font-size:10.5px;width:109px;height:28px;line-height:28px}

  .partners{position:absolute;top:908px;left:0;width:1200px;height:72px;border-top:1px solid var(--line)}
  .partners .wrap{display:flex;justify-content:space-between;align-items:center;height:72px;padding:0 14px}
  .partner-badge{width:92px;height:34px;background:#cfcfcf;border-radius:4px}

  .site-footer{position:absolute;top:980px;left:0;width:1200px;height:45px;background:var(--orange);color:var(--white)}
  .site-footer .wrap{display:flex;justify-content:space-between;align-items:center;height:45px;font-size:8px;text-transform:uppercase}
  .foot-nav{display:flex}
  .foot-nav span{padding:0 11px;border-left:1px solid rgba(255,255,255,.7)}
  .foot-nav span:first-child{padding-left:1px;border:0}
</style>
</head>
<body>
<header class="site-header">
  <div class="wrap">
    <div class="brand">
      <div class="brand-mark"></div>
      <div class="brand-name">The Halvern Group</div>
    </div>
    <div class="follow"><span>FOLLOW US :</span><i class="social s1"></i><i class="social s2"></i><i class="social s3"></i><i class="social s4"></i></div>
  </div>
</header>

<nav class="main-nav">
  <ul>
    <li class="active" style="width:87px">Home</li>
    <li style="width:96px">About</li>
    <li style="width:97px">People</li>
    <li style="width:107px">Services</li>
    <li style="width:102px">Sectors</li>
    <li style="width:107px">Careers</li>
    <li style="width:125px">Key Partners</li>
    <li style="width:117px">Contact</li>
  </ul>
</nav>

<section class="hero" role="img" aria-label="Photo of smiling consultant in a bright office with colleagues talking in the background">
  <div class="hero-arrow prev"><svg viewBox="0 0 48 48"><path d="M29 14 L17 24 L29 34Z" fill="rgba(120,90,70,.35)"/></svg></div>
  <div class="hero-arrow next"><svg viewBox="0 0 48 48"><path d="M19 14 L31 24 L19 34Z" fill="rgba(200,150,120,.35)"/></svg></div>
  <div class="caption one">We work with organisations</div>
  <div class="caption two">Find and implement creative and sensible solutions...</div>
</section>

<main class="wrap">
  <section class="welcome">
    <h1>Welcome to The Halvern Group</h1>
    <p>It is a long established fact that a reader will be distracted by the readable content of a page when looking at its layout. The point of using Lorem Ipsum is that it has a more-or-less normal distribution of letters, as opposed to using 'Content here, content here', making it look like readable English.</p>
  </section>

  <section class="pillars">
    <article class="pillar">
      <svg viewBox="0 0 60 56"><path d="M4 20 L18 14 L30 20 L42 14 L56 20 L56 32 L46 40 L36 44 L28 40 L12 36 L4 32Z" fill="var(--orange)"/></svg>
      <h2>Ideas and partnerships</h2>
      <p>Many desktop publishing packages and web page editors now use Lorem Ipsum as their default model text, and a search for 'lorem ipsum' will uncover many web sites still in uncover many web sites still intheir...</p>
      <a class="btn">Read More</a>
    </article>
    <article class="pillar">
      <svg viewBox="0 0 60 56"><circle cx="30" cy="14" r="8" fill="none" stroke="var(--orange)" stroke-width="2"/><circle cx="14" cy="30" r="5" fill="var(--orange)"/><path d="M6 52 V42 Q14 34 22 42 V52Z" fill="var(--orange)"/><circle cx="46" cy="30" r="5" fill="var(--orange)"/><path d="M38 52 V42 Q46 34 54 42 V52Z" fill="var(--orange)"/></svg>
      <h2>Knowledgeable leaders</h2>
      <p>Many desktop publishing packages and web page editors now use Lorem Ipsum as their default model text, and a search for 'lorem ipsum' will uncover many web sites still in uncover many web sites still intheir...</p>
      <a class="btn">Read More</a>
    </article>
    <article class="pillar">
      <svg viewBox="0 0 60 56"><path d="M22 54 V44 Q10 40 12 24 Q14 4 32 4 Q50 6 48 26 L52 34 L46 36 V46 L36 46 V54" fill="none" stroke="var(--orange)" stroke-width="2"/><circle cx="32" cy="22" r="7" fill="none" stroke="var(--orange)" stroke-width="2"/></svg>
      <h2>Solutions</h2>
      <p>Many desktop publishing packages and web page editors now use Lorem Ipsum as their default model text, and a search for 'lorem ipsum' will uncover many web sites still in uncover many web sites still intheir...</p>
      <a class="btn">Read More</a>
    </article>
  </section>
</main>

<section class="partners">
  <div class="wrap">
    <i class="partner-badge"></i><i class="partner-badge" style="width:56px"></i><i class="partner-badge"></i><i class="partner-badge" style="width:70px"></i><i class="partner-badge" style="width:80px"></i><i class="partner-badge"></i><i class="partner-badge" style="width:120px"></i>
  </div>
</section>

<footer class="site-footer">
  <div class="wrap">
    <div class="foot-nav"><span>Home</span><span>About</span><span>People</span><span>Services</span><span>Sectors</span><span>Careers</span><span>Key Partners</span><span>Contact</span></div>
    <div>Copyright © 2013. The Halvern Group. All rights reserved.</div>
  </div>
</footer>
</body>
</html>
```